custom carpentry, woodworking and home repair company needs logo design and business card design

Attention: I apologize but I just received notification from my state that I cannot use the company name that I originally submitted (Beyond The Bench). The new name will be Joinolux We need a company logo and business card design for our new company based in the Hampton Roads area of Virginia. The company name is Joinolux. The final design should give a first impression of true craftsmanship and attention to detail. We would like the card to include the company name, my name Mark Tellman (owner), phone number (757) 348-2615, website (joinolux-example.com) and email address (mark@joinolux-example.com). Everything else is up to your discretion. Thanks, have fun, and good luck.

Industry/Entity Type

Business

Contact Information for Business Card

See project description

Logo Text

see project description

Colors

Designer to choose colors to be used in the design.

```html
<!DOCTYPE html>
<html lang="en">
<head>
<meta charset="utf-8">
<title>Joinolux Business Card</title>
<link href="https://fonts.googleapis.com/css2?family=Arimo:wght@400;700&display=swap" rel="stylesheet">
<style>
  :root {
    --page: #e9e7e3;
    --paper: #ffffff;
    --ink: #1b1b1b;
    --wood: #8a5a32;
    --wood-light: #b07c4c;
    --night: #050505;
    --silver: #9a9a9a;
    --rule: #444444;
  }
  * { margin: 0; padding: 0; box-sizing: border-box; }
  html, body { width: 1200px; height: 900px; overflow: hidden; }
  body {
    background: var(--page);
    font-family: "Arimo", Arial, sans-serif;
    color: var(--ink);
    display: flex;
    align-items: center;
    justify-content: center;
    gap: 50px;
  }
  .card {
    position: relative;
    width: 540px;
    height: 310px;
    box-shadow: 0 6px 18px rgba(0,0,0,0.18);
    overflow: hidden;
  }
  .card-front { background: var(--paper); }
  .card-back { background: var(--night); display: flex; flex-direction: column; align-items: center; justify-content: center; }

  .front-art { position: absolute; inset: 0; }

  .brand-small {
    position: absolute; left: 22px; top: 16px;
    display: flex; flex-direction: column; align-items: center; gap: 3px;
  }
  .brand-small .mark {
    width: 28px; height: 28px; border-radius: 50%; background: var(--wood);
  }
  .brand-small .name {
    font-size: 11px; color: var(--wood); letter-spacing: 0.5px; text-transform: uppercase;
  }

  .contact-list {
    position: absolute; left: 22px; top: 92px;
    list-style: none; display: flex; flex-direction: column; gap: 5px;
    font-size: 12px; line-height: 1.15;
  }
  .contact-list li { display: flex; align-items: flex-start; gap: 8px; }
  .contact-list svg { width: 14px; height: 14px; flex: none; fill: none; stroke: var(--ink); stroke-width: 1.4; }
  .contact-list .address svg { fill: var(--ink); stroke: none; }

  .person {
    position: absolute; right: 22px; top: 210px; text-align: right;
    border-bottom: 2px solid var(--wood); padding: 0 4px 3px 40px;
  }
  .person .full-name { font-size: 17px; color: var(--ink); }
  .person .role { font-size: 10px; color: var(--ink); }

  .back-mark { width: 82px; height: 82px; border-radius: 50%; background: #ffffff; }
  .back-name {
    margin-top: 10px; font-size: 34px; letter-spacing: 2px; color: var(--silver); text-transform: uppercase;
  }
</style>
</head>
<body>
  <section class="card card-front" aria-label="Business card front">
    <svg class="front-art" viewBox="0 0 540 310" aria-hidden="true">
      <line x1="95" y1="0" x2="480" y2="216" stroke="var(--rule)" stroke-width="0.8"/>
      <polygon points="0,218 0,232 150,310 176,310" fill="var(--night)"/>
      <polygon points="0,232 0,246 124,310 150,310" fill="var(--wood-light)"/>
    </svg>

    <div class="brand-small">
      <span class="mark"></span>
      <span class="name">Joinolux</span>
    </div>

    <ul class="contact-list">
      <li class="address">
        <svg viewBox="0 0 14 14"><path d="M7 1 L13 7 H11 V13 H3 V7 H1 Z"/></svg>
        <span>Suite 12,<br>40 Harbor Lane,</span>
      </li>
      <li>
        <svg viewBox="0 0 14 14"><path d="M2 5 Q7 1 12 5 L11 7 H9 V5.5 H5 V7 H3 Z M3 8 H11 V12 H3 Z"/></svg>
        <span>(757) 348-2615</span>
      </li>
      <li>
        <svg viewBox="0 0 14 14"><rect x="3" y="1.5" width="8" height="11" rx="1"/></svg>
        <span>(757) 348-2616</span>
      </li>
      <li>
        <svg viewBox="0 0 14 14"><rect x="1" y="3" width="12" height="8"/><path d="M1 3 L7 8 L13 3"/></svg>
        <span>Email: mark@joinolux-example.com</span>
      </li>
      <li>
        <svg viewBox="0 0 14 14"><circle cx="7" cy="7" r="5.5"/><path d="M1.5 7 H12.5 M7 1.5 Q3.5 7 7 12.5 M7 1.5 Q10.5 7 7 12.5"/></svg>
        <span>www.joinolux-example.com</span>
      </li>
    </ul>

    <div class="person">
      <div class="full-name">Mark Tellman</div>
      <div class="role">Chief Executive Officer</div>
    </div>
  </section>

  <section class="card card-back" aria-label="Business card back">
    <span class="back-mark"></span>
    <span class="back-name">Joinolux</span>
  </section>
</body>
</html>
```